"Brighter Harbors: Ways to guide growth via study" Co Authored by Dr Malcolm Penner & Lewis Brandt

We need a clean design book cover for "Brighter Harbors: Ways to guide growth via study." Co-authored by Dr Malcolm Penner and Lewis Brandt. (Malcolm Penner being the lead author)
This book tells the story of a new learning paradigm in business for successful transformation. Why and How you can make learning last.
We would like the design to work with - but not limited by - the current branding that we already have in place; please see www.drmalcolmpenner.example

Target Market(s)

Business decision makers.

Industry/Entity Type

Learning

Font styles to use
Sans Serif

Requirements
Must have
• A clean professional finish
Nice to have
• A picture, graphic or image of some sort tied to the brief
Should not have
• Be too busy in design.

```html
<!DOCTYPE html>
<html lang="en">
<head>
<meta charset="utf-8">
<title>Brighter Harbors: Ways to guide growth via study</title>
<link rel="stylesheet" href="https://fonts.googleapis.com/css2?family=Montserrat:wght@800;900&family=Roboto+Condensed:wght@400&display=swap">
<style>
  :root {
    --navy-deep: #0d2a4b;
    --navy: #1a4674;
    --navy-text: #143a63;
    --grey-sub: #7b7b7b;
    --paper: #ffffff;
    --paper-edge: #e9e9e9;
    --orange: #f08a1c;
    --amber: #f7b733;
    --blue-ribbon: #3f6fa8;
  }
  html, body {
    margin: 0;
    padding: 0;
    width: 798px;
    height: 1200px;
    overflow: hidden;
  }
  .cover {
    position: relative;
    width: 798px;
    height: 1200px;
    overflow: hidden;
    background: radial-gradient(ellipse at 50% 45%, var(--paper) 55%, var(--paper-edge) 100%);
    font-family: "Montserrat", sans-serif;
  }
  .cover__title {
    position: absolute;
    left: 0;
    top: 0;
    width: 798px;
    height: 300px;
  }
  .cover__title text {
    font-family: "Montserrat", sans-serif;
    font-weight: 900;
    font-size: 158px;
  }
  .cover__subtitle {
    position: absolute;
    left: 0;
    right: 0;
    top: 348px;
    margin: 0;
    text-align: center;
    font-family: "Roboto Condensed", sans-serif;
    font-weight: 400;
    font-size: 35px;
    color: var(--grey-sub);
  }
  .cover__artwork {
    position: absolute;
    left: 0;
    top: 410px;
    width: 660px;
    height: 620px;
    background:
      radial-gradient(circle at 55% 50%, var(--amber) 0%, var(--orange) 32%, rgba(240,138,28,0.25) 52%, rgba(255,255,255,0) 70%),
      linear-gradient(160deg, rgba(63,111,168,0.35) 0%, rgba(255,255,255,0) 40%);
  }
  .cover__authors {
    position: absolute;
    left: 0;
    right: 0;
    top: 1058px;
    margin: 0;
    text-align: center;
    font-weight: 800;
    font-size: 42px;
    line-height: 60px;
    color: var(--navy-text);
  }
  .cover__authors span { display: block; }
</style>
</head>
<body>
<main class="cover">
  <h1 class="cover__title" aria-label="Brighter Harbors">
    <svg width="798" height="300" viewBox="0 0 798 300" aria-hidden="true">
      <defs>
        <linearGradient id="titleInk" x1="0" y1="0" x2="1" y2="1">
          <stop offset="0" stop-color="#0d2a4b"/>
          <stop offset="0.5" stop-color="#1a4674"/>
          <stop offset="1" stop-color="#0f3158"/>
        </linearGradient>
      </defs>
      <text x="27" y="133" textLength="745" lengthAdjust="spacingAndGlyphs" fill="url(#titleInk)">BRIGHTER</text>
      <text x="27" y="282" textLength="745" lengthAdjust="spacingAndGlyphs" fill="url(#titleInk)">HARBORS</text>
    </svg>
  </h1>
  <p class="cover__subtitle">Ways to guide growth via study</p>
  <div class="cover__artwork" role="img" aria-label="Illustration of an orange and yellow swirled head in profile set on a measuring dial, with folded ribbons of orange, yellow and blue streaming from behind it"></div>
  <p class="cover__authors">
    <span>Dr Malcolm Penner</span>
    <span>and Lewis Brandt</span>
  </p>
</main>
</body>
</html>
```